Student project platform needs an awareness flyer

Tunvelo is a matchmaking and crowdfunding site for student projects. On this platform, students can team up with each other to invent a new product, innovate, or start a business. They can also raise funds for their project.

** I am in need of an 8x11" flyer to print and distribute digitally which notifies students of all different skill sets that this site exists.

The flyer should communicate that a diverse user base is being built on this site, with people who have skills in programming, engineering, design, business, finance, and so on.

The flyer should also be clean and modern, with an emphasis on creativity and innovation. I've attached the business' logo to give you an idea of the artistic style we have already established.

Target Market(s)

University students

Industry/Entity Type

Crowdfunding

Font styles to use
Serif
Sans Serif

Requirements
Must have
• * Clean and modern design
• * Color scheme of my logo: #336699 and #669933 (blue and green)
• * Convey that this site is for people of different skill sets: programming, engineering, design, business, finance, and so on.
• * See the attached "Tunvelo Copy.txt" for text to include on the flyer

```html
<!DOCTYPE html>
<html lang="en">
<head>
<meta charset="utf-8">
<title>Tunvelo Flyer</title>
<link rel="stylesheet" href="https://fonts.googleapis.com/css2?family=Open+Sans:wght@400;600;700;800&display=swap">
<style>
  :root {
    --blue: #336699;
    --blue-dark: #2a5a8c;
    --green: #669933;
    --ink: #1d1d1d;
    --paper: #ffffff;
    --stage: #6a6a6a;
    --photo-a: #e9e4df;
    --photo-b: #b9a89a;
    --photo-c: #8fa5b8;
  }
  * { box-sizing: border-box; margin: 0; padding: 0; }
  html, body { width: 850px; height: 1200px; overflow: hidden; }
  body {
    background: var(--stage);
    font-family: "Open Sans", Arial, sans-serif;
    color: var(--ink);
    position: relative;
  }
  .flyer {
    position: absolute;
    left: 25px; top: 52px;
    width: 800px; height: 1095px;
    background: var(--paper);
    box-shadow: 0 6px 18px rgba(0,0,0,.35);
    overflow: hidden;
  }
  .hero { position: absolute; left: 0; top: 0; width: 800px; height: 460px; }

  .brand { position: absolute; left: 36px; top: 378px; width: 260px; text-align: center; }
  .brand-dot {
    width: 96px; height: 96px; border-radius: 50%;
    background: var(--blue); margin: 0 auto 22px;
  }
  .brand-name { font-size: 50px; font-weight: 600; color: var(--blue); letter-spacing: 1px; line-height: 1; }

  .callout {
    position: absolute; left: 38px; top: 596px;
    font-size: 24px; font-weight: 600; line-height: 34px;
    color: var(--blue); text-transform: uppercase;
  }
  .callout strong { color: var(--green); font-weight: 700; }

  .about-band {
    position: absolute; left: 0; top: 743px;
    width: 345px; height: 44px;
    background: var(--green);
    border-radius: 0 22px 22px 0;
    color: #fff; font-size: 27px; font-weight: 700;
    line-height: 44px; padding-left: 38px;
  }
  .about-text {
    position: absolute; left: 38px; top: 802px;
    font-size: 23px; line-height: 34px; color: var(--ink);
  }

  .join { position: absolute; right: 38px; top: 462px; text-align: right; }
  .join-title { font-size: 72px; font-weight: 700; color: var(--blue); line-height: 1; }
  .join-name { font-size: 44px; font-weight: 700; color: var(--green); line-height: 1.05; margin-top: 2px; }
  .join-text {
    font-size: 26px; line-height: 35px; text-transform: uppercase;
    color: var(--ink); font-weight: 400; margin-top: 2px;
  }
  .join-text strong { font-weight: 700; }

  .skills { position: absolute; left: 512px; top: 692px; width: 252px; }
  .skills-title {
    font-size: 46px; font-weight: 700; color: var(--green);
    line-height: 1; padding-bottom: 10px;
    border-bottom: 2px solid #c9c9c9; text-align: right;
  }
  .skill-list { list-style: none; margin-top: 20px; position: relative; }
  .skill-list::before {
    content: ""; position: absolute; left: 17px; top: 18px; bottom: 18px;
    width: 2px; background: var(--blue);
  }
  .skill {
    position: relative; display: flex; align-items: center;
    height: 50px; font-size: 31px; color: var(--ink);
  }
  .skill-num {
    width: 36px; height: 36px; border-radius: 50%;
    background: var(--blue); color: #fff;
    font-size: 21px; font-weight: 600;
    display: flex; align-items: center; justify-content: center;
    margin-right: 16px; position: relative;
    box-shadow: 0 0 0 3px #fff;
  }

  .footer {
    position: absolute; left: 38px; right: 38px; top: 1050px;
    display: flex; align-items: center; gap: 18px;
  }
  .footer-rule { flex: 1; height: 2px; background: #777; }
  .footer-url { font-size: 26px; font-weight: 600; color: var(--green); }
</style>
</head>
<body>
  <main class="flyer">
    <svg class="hero" viewBox="0 0 800 460" aria-hidden="false">
      <defs>
        <linearGradient id="photoTone" x1="0" y1="0" x2="1" y2="1">
          <stop offset="0" stop-color="var(--photo-a)"/>
          <stop offset="0.55" stop-color="var(--photo-b)"/>
          <stop offset="1" stop-color="var(--photo-c)"/>
        </linearGradient>
      </defs>
      <path role="img" aria-label="Photo of a diverse group of smiling students stacking their hands together in the centre"
            d="M0,0 H800 V440 C720,420 650,360 560,332 C470,304 430,338 330,352 C200,370 120,300 0,290 Z"
            fill="url(#photoTone)"/>
      <path d="M0,300 C120,312 200,382 330,364 C430,350 470,318 560,344 C650,372 720,432 800,452"
            fill="none" stroke="#dbe6f0" stroke-width="14"/>
      <path d="M0,290 C120,300 200,370 330,352 C430,338 470,304 560,332 C650,360 720,420 800,440"
            fill="none" stroke="var(--blue)" stroke-width="9"/>
    </svg>

    <div class="brand">
      <div class="brand-dot"></div>
      <div class="brand-name">TUNVELO</div>
    </div>

    <p class="callout">
      Calling all students<br>
      who want to <strong>build,</strong><br>
      <strong>innovate, invent,</strong><br>
      <strong>or start a business</strong>
    </p>

    <h2 class="about-band">WHAT IS TUNVELO?</h2>
    <p class="about-text">
      Tunvelo is a matchmaking<br>
      and crowdfunding platform<br>
      for student projects.<br>
      It allows students to form<br>
      teams of diverse skills<br>
      and raise money to build,<br>
      innovate, invent,<br>
      or start a business.
    </p>

    <section class="join">
      <h1 class="join-title">JOIN</h1>
      <div class="join-name">TUNVELO</div>
      <p class="join-text">
        To <strong>support</strong> and <strong>lend</strong><br>
        your <strong>skills to student</strong><br>
        <strong>projects!</strong>
      </p>
    </section>

    <section class="skills">
      <h2 class="skills-title">Our Skills</h2>
      <ol class="skill-list">
        <li class="skill"><span class="skill-num">1</span>Programming</li>
        <li class="skill"><span class="skill-num">2</span>Engineering</li>
        <li class="skill"><span class="skill-num">3</span>Design</li>
        <li class="skill"><span class="skill-num">4</span>Business</li>
        <li class="skill"><span class="skill-num">5</span>Finance</li>
      </ol>
    </section>

    <footer class="footer">
      <span class="footer-rule"></span>
      <span class="footer-url">www. tunvelo.com</span>
      <span class="footer-rule"></span>
    </footer>
  </main>
</body>
</html>
```